Packaging design for a reclosable bag for our product

We have a logo, and we need to put it on packaging for our product and while we want the look to be simple, we want it to follow good design principles and also contain spaces for other product descriptions.

There will be 5 sizes at launch so I'd like 5 variations, one for each size.

I've included a few mockups of the type of bag that I made but they are all just rough ideas that I had.

I want the brand to look scientific and methodical and even a bit quirky, as in "wow this is a serious product but also a bit unusual."

```html
<!DOCTYPE html>
<html lang="en">
<head>
<meta charset="utf-8">
<title>Bias Lighting Bag – Extra Large</title>
<link rel="stylesheet" href="https://fonts.googleapis.com/css2?family=Montserrat:wght@500;700&display=swap">
<style>
  :root {
    --ink: #0d0d0d;
    --bag: #ececec;
    --paper: #ffffff;
    --backdrop: #bdbdbd;
  }
  html, body {
    margin: 0;
    width: 1200px;
    height: 960px;
    overflow: hidden;
    background: var(--backdrop);
  }
  .stage {
    position: relative;
    width: 1200px;
    height: 960px;
  }
  .bag {
    position: absolute;
    left: 290px;
    top: 60px;
    width: 620px;
    height: 840px;
    font-family: "Montserrat", sans-serif;
    color: var(--paper);
    box-shadow: 0 10px 30px rgba(0,0,0,0.18);
  }
  .bag-art {
    position: absolute;
    inset: 0;
  }
  .product-title {
    position: absolute;
    left: 38px;
    top: 500px;
    margin: 0;
    font-weight: 700;
    font-size: 46px;
    letter-spacing: 1px;
    line-height: 1;
  }
  .size-spec, .light-spec {
    position: absolute;
    left: 38px;
    margin: 0;
    font-weight: 500;
    letter-spacing: 1px;
    line-height: 1.15;
  }
  .size-spec { top: 568px; font-size: 26px; }
  .light-spec { top: 660px; font-size: 25px; }
  .brand-name {
    position: absolute;
    left: 542px;
    top: 640px;
    transform: translate(-50%, -50%) rotate(90deg);
    margin: 0;
    font-weight: 700;
    font-size: 150px;
    letter-spacing: 4px;
    line-height: 1;
    color: var(--ink);
    white-space: nowrap;
  }
</style>
</head>
<body>
<main class="stage">
  <section class="bag">
    <svg class="bag-art" width="620" height="840" viewBox="0 0 620 840" aria-hidden="true">
      <rect class="bag-body" width="620" height="840" fill="var(--bag)"/>
      <polygon class="corner-band" points="0,0 260,0 0,150" fill="var(--ink)"/>
      <polygon class="top-band" points="400,175 620,95 620,140 470,200 400,200" fill="var(--ink)"/>
      <polygon class="main-panel" points="0,330 400,175 400,210 465,210 465,840 0,840" fill="var(--ink)"/>
      <rect class="handle-slot" x="255" y="85" width="120" height="32" rx="16" fill="var(--backdrop)"/>
    </svg>
    <h1 class="product-title">BIAS LIGHTING</h1>
    <p class="size-spec">EXTRA LARGE<br>5 METERS</p>
    <p class="light-spec">SIMULATED D65 CRI 90+<br>6500K WHITE BIAS LIGHTING</p>
    <p class="brand-name">NR4</p>
  </section>
</main>
</body>
</html>
```